Unusual Options Activity Graphic Card Design for Finance App

We are developing a financial data platform called Vantix Pulse, and we need a visually striking, mobile-optimized graphic card design to display unusual options activity. The card will be featured in our mobile app and marketing materials, inspired by platforms like Marlocq and Pindrake Lane.
🔹 Design Goals:
Modern, clean, and professional aesthetic
Use vibrant electric blue, green, or dark theme gradients
Must feel tech-savvy and finance-oriented
Layout should be optimized for vertical mobile format (portrait)
🔹 Information to Include in the Card:
Ticker Symbol (e.g., QZR) with colored badge
Date & Time of trade
Trade Type (e.g., Sweep Call / Put)
Execution Type (At Ask or At Bid)
Strike Price
Expiration Date
Premium (e.g., $342.75K)
Size@Price (e.g., 6995@$0.49)
Volume
Open Interest
Branding at bottom: “Vantix Pulse” in modern font
🔹 Inspiration:
Marlocq’s profit/loss cards
Clean fintech dashboards (Quillmere, Pindrake Lane, Haskvorn Console)
Please provide the final deliverable in high-resolution PNG and layered PSD or Figma file for future edits.
Stock Market Traders
Finance

```html
<!DOCTYPE html>
<html lang="en">
<head>
<meta charset="utf-8">
<title>Vantix Pulse – Unusual Options Activity Cards</title>
<link href="https://fonts.googleapis.com/css2?family=Poppins:wght@400;500;600;700&display=swap" rel="stylesheet">
<style>
  :root{
    --stage-edge:#0b2f3f;
    --stage-mid:#11545a;
    --card-base:#0a141b;
    --card-navy:#121d33;
    --accent:#2fd14a;
    --accent-bright:#39e25a;
    --accent-deep:#0f7a2a;
    --text:#f2f6f4;
    --label:#36d452;
    --panel:rgba(10,16,22,0.82);
    --grid:rgba(150,60,110,0.35);
    --candle-up:rgba(40,190,70,0.55);
    --candle-down:rgba(170,40,80,0.45);
  }
  *{margin:0;padding:0;box-sizing:border-box}
  html,body{width:1200px;height:675px;overflow:hidden}
  body{
    font-family:"Poppins",sans-serif;
    background:
      radial-gradient(ellipse 60% 55% at 50% 50%, rgba(40,170,90,0.35), transparent 70%),
      radial-gradient(ellipse 90% 80% at 50% 10%, var(--stage-mid), var(--stage-edge));
    position:relative;
  }
  .option-card{
    position:absolute;top:67px;width:342px;height:541px;overflow:hidden;
    background:
      radial-gradient(ellipse 70% 45% at 60% 52%, rgba(60,190,70,0.45), transparent 70%),
      linear-gradient(180deg,var(--card-base) 0%,#0c1a18 45%,var(--card-navy) 100%);
    box-shadow:0 10px 40px rgba(0,0,0,0.35);
  }
  .option-card--chart{left:202px}
  .option-card--clean{left:657px}
  .chart-backdrop{position:absolute;inset:0}
  .trade-header{
    position:absolute;left:32px;top:30px;width:277px;height:36px;
    border:1px solid rgba(57,226,90,0.7);border-radius:5px;
    background:linear-gradient(90deg,rgba(10,30,18,0.9) 0%,rgba(20,110,40,0.8) 55%,var(--accent-bright) 100%);
  }
  .ticker-badge{
    position:absolute;left:6px;top:5px;width:51px;height:24px;border-radius:3px;
    background:var(--accent-bright);color:#06130a;
    font-weight:600;font-size:16px;line-height:24px;text-align:center;
  }
  .trade-time{
    position:absolute;right:12px;top:0;line-height:34px;
    color:var(--text);font-size:14px;font-weight:500;word-spacing:8px;
  }
  .trade-type{
    position:absolute;left:34px;top:80px;color:var(--text);
    font-size:24px;font-weight:500;line-height:1;letter-spacing:0.3px;
  }
  .execution-type{
    position:absolute;left:35px;top:107px;color:var(--accent);
    font-size:16px;font-weight:500;line-height:1;
  }
  .hero-visual{
    position:absolute;left:45px;top:130px;width:260px;height:250px;border-radius:50%;
    background:radial-gradient(ellipse at 55% 50%,rgba(160,240,150,0.55) 0%,rgba(60,200,80,0.35) 35%,rgba(20,90,40,0.1) 65%,transparent 75%);
  }
  .trade-details{
    position:absolute;left:13px;top:421px;width:316px;height:71px;border-radius:8px;
    background:var(--panel);
  }
  .detail-row{position:absolute;font-size:10.5px;line-height:14px;white-space:nowrap}
  .detail-label{color:var(--label)}
  .detail-value{color:var(--text)}
  .col-a-label{left:21px}.col-a-value{left:91px}
  .col-b-label{left:173px}.col-b-value{right:21px;text-align:right}
  .r1{top:13px}.r2{top:28px}.r3{top:43px}
  .brand-name{
    position:absolute;left:0;right:0;top:503px;text-align:center;
    color:var(--text);font-weight:700;font-size:15px;letter-spacing:1.5px;
  }
</style>
</head>
<body>

<article class="option-card option-card--chart">
  <svg class="chart-backdrop" width="342" height="541" viewBox="0 0 342 541" aria-hidden="true">
    <g stroke="var(--grid)" stroke-width="1">
      <line x1="0" y1="10" x2="342" y2="0"/><line x1="0" y1="95" x2="342" y2="85"/>
      <line x1="0" y1="205" x2="342" y2="195"/><line x1="0" y1="330" x2="342" y2="320"/>
      <line x1="0" y1="445" x2="342" y2="435"/><line x1="0" y1="530" x2="342" y2="520"/>
      <line x1="10" y1="0" x2="15" y2="541"/><line x1="110" y1="0" x2="115" y2="541"/>
      <line x1="230" y1="0" x2="235" y2="541"/><line x1="330" y1="0" x2="335" y2="541"/>
    </g>
    <g fill="var(--candle-up)">
      <rect x="12" y="200" width="5" height="50"/><rect x="26" y="240" width="4" height="40"/>
      <rect x="68" y="225" width="5" height="45"/><rect x="88" y="200" width="4" height="55"/>
      <rect x="138" y="120" width="5" height="90"/><rect x="162" y="110" width="4" height="60"/>
      <rect x="178" y="130" width="5" height="70"/><rect x="232" y="150" width="5" height="60"/>
      <rect x="282" y="85" width="6" height="70"/><rect x="300" y="110" width="4" height="50"/>
      <rect x="318" y="100" width="6" height="60"/>
    </g>
    <g fill="var(--candle-down)">
      <rect x="2" y="230" width="4" height="40"/><rect x="48" y="250" width="4" height="30"/>
      <rect x="152" y="135" width="4" height="20"/><rect x="266" y="125" width="5" height="40"/>
    </g>
  </svg>
  <div class="trade-header">
    <span class="ticker-badge">QZR</span>
    <span class="trade-time">04/19/2025 10:30</span>
  </div>
  <h2 class="trade-type">SWEEP CALL</h2>
  <p class="execution-type">AT ASK</p>
  <div class="hero-visual" role="img" aria-label="Glossy 3D green upward arrow surrounded by floating green question marks"></div>
  <div class="trade-details">
    <span class="detail-row detail-label col-a-label r1">Strike Price</span>
    <span class="detail-row detail-value col-a-value r1">$10</span>
    <span class="detail-row detail-label col-a-label r2">Premium</span>
    <span class="detail-row detail-value col-a-value r2">$342.75K</span>
    <span class="detail-row detail-label col-a-label r3">Size@Price</span>
    <span class="detail-row detail-value col-a-value r3">6995@0.49</span>
    <span class="detail-row detail-label col-b-label r1">Expiration</span>
    <span class="detail-row detail-value col-b-value r1">Apr 28 2025</span>
    <span class="detail-row detail-label col-b-label r2">Volume</span>
    <span class="detail-row detail-value col-b-value r2">0000</span>
    <span class="detail-row detail-label col-b-label r3">Open Interest</span>
    <span class="detail-row detail-value col-b-value r3">0000</span>
  </div>
  <p class="brand-name">VANTIX PULSE</p>
</article>

<article class="option-card option-card--clean">
  <div class="trade-header">
    <span class="ticker-badge">QZR</span>
    <span class="trade-time">04/19/2025 10:30</span>
  </div>
  <h2 class="trade-type">SWEEP CALL</h2>
  <p class="execution-type">AT ASK</p>
  <div class="hero-visual" role="img" aria-label="Glossy 3D green upward arrow surrounded by floating green question marks"></div>
  <div class="trade-details">
    <span class="detail-row detail-label col-a-label r1">Strike Price</span>
    <span class="detail-row detail-value col-a-value r1">$10</span>
    <span class="detail-row detail-label col-a-label r2">Premium</span>
    <span class="detail-row detail-value col-a-value r2">$342.75K</span>
    <span class="detail-row detail-label col-a-label r3">Size@Price</span>
    <span class="detail-row detail-value col-a-value r3">6995@0.49</span>
    <span class="detail-row detail-label col-b-label r1">Expiration</span>
    <span class="detail-row detail-value col-b-value r1">Apr 28 2025</span>
    <span class="detail-row detail-label col-b-label r2">Volume</span>
    <span class="detail-row detail-value col-b-value r2">0000</span>
    <span class="detail-row detail-label col-b-label r3">Open Interest</span>
    <span class="detail-row detail-value col-b-value r3">0000</span>
  </div>
  <p class="brand-name">VANTIX PULSE</p>
</article>

</body>
</html>
```